Webdesign für Branchenverzeichnis
Zielgruppe
Wir-bauen-Brücken – das Branchenverzeichnis der Selbstverantwortlichen.
Der Anbieter präsentiert sich mit seinem Namen und der URL - ähnlich wie bei 'blaue Listen' oder Jobhafen.
Aufgabenstellung
Das Branchenverzeichnis sollte neutral und gleichzeitig hochwertig sein. Die Hauptfarben sind Gold, Schwarz und Weiß. Logo und Corporate Design wurden bereits entwickelt

```html
<!DOCTYPE html>
<html lang="de">
<head>
<meta charset="utf-8">
<title>Wir bauen Brücken – Branchenverzeichnis</title>
<link rel="stylesheet" href="https://fonts.googleapis.com/css2?family=Quicksand:wght@400;500;600;700&family=Montserrat:wght@500;600&family=Jost:wght@300;400;500&display=swap">
<style>
  :root {
    --gold: #d4b262;
    --gold-light: #e8d5a4;
    --gold-pale: #f7ebc4;
    --cream: #fffbe8;
    --white: #ffffff;
    --ink: #111111;
    --nav: #3a3a3a;
    --dark-top: #5e5e5e;
    --dark-bottom: #1e1e1e;
    --muted: #6b6b6b;
    --btn-dark: #3b3b3b;
  }
  * { box-sizing: border-box; margin: 0; padding: 0; }
  html, body { width: 1200px; height: 2301px; overflow: hidden; }
  body { position: relative; background: var(--cream); font-family: "Jost", sans-serif; color: var(--ink); }
  .abs { position: absolute; }

  /* Navigation */
  .topbar { position: absolute; left: 0; top: 0; width: 1200px; height: 62px; background: var(--nav); z-index: 5; }
  .brand { position: absolute; left: 156px; top: 17px; display: flex; align-items: center; gap: 6px; }
  .brand-dot { width: 16px; height: 16px; border-radius: 50%; border: 2px solid var(--gold); }
  .brand-name { font-family: "Quicksand", sans-serif; font-weight: 600; font-size: 12px; color: var(--gold); line-height: 1.1; width: 60px; }
  .nav-link { position: absolute; top: 25px; font-family: "Montserrat", sans-serif; font-weight: 600; font-size: 9.5px; letter-spacing: 1px; color: var(--white); }
  .nav-link.is-active { color: var(--gold); }
  .social { position: absolute; top: 24px; width: 12px; height: 12px; border-radius: 50%; background: var(--white); }
  .nav-cta { position: absolute; left: 918px; top: 17px; width: 126px; height: 28px; background: var(--gold); color: var(--white); font-family: "Montserrat", sans-serif; font-size: 8.5px; letter-spacing: .6px; display: flex; align-items: center; justify-content: center; }

  /* Hero */
  .hero { position: absolute; left: 0; top: 62px; width: 1200px; height: 490px; background: #fdfdfc; overflow: hidden; }
  .hero-title { position: absolute; left: 156px; top: 100px; font-family: "Quicksand", sans-serif; font-weight: 700; font-size: 33px; letter-spacing: 2px; }
  .accent { color: var(--gold); }
  .hero-sub { position: absolute; left: 156px; top: 140px; font-family: "Quicksand", sans-serif; font-size: 15.5px; letter-spacing: .6px; }
  .hero-text { position: absolute; left: 159px; top: 172px; width: 385px; font-size: 11px; line-height: 17px; color: var(--muted); letter-spacing: .3px; font-family: "Quicksand", sans-serif; }
  .btn { position: absolute; display: flex; align-items: center; justify-content: center; font-size: 10.5px; letter-spacing: .6px; font-family: "Jost", sans-serif; }
  .btn-gold { left: 157px; top: 286px; width: 157px; height: 38px; background: var(--gold); color: var(--white); }
  .btn-outline { left: 347px; top: 286px; width: 129px; height: 38px; border: 1.5px solid var(--gold-light); color: var(--ink); }

  /* Search */
  .search { position: absolute; left: 156px; top: 490px; width: 888px; height: 125px; background: var(--gold); box-shadow: 0 6px 14px rgba(0,0,0,.12); z-index: 3; }
  .field { position: absolute; top: 44px; width: 187px; height: 37px; background: var(--white); border: 1px solid #e3d6b2; font-size: 9px; color: #8a8a8a; display: flex; align-items: center; padding-left: 13px; }
  .field svg { position: absolute; right: 12px; top: 10px; }
  .search-btn { position: absolute; left: 725px; top: 44px; width: 125px; height: 37px; background: var(--btn-dark); color: var(--white); font-size: 9px; letter-spacing: .6px; display: flex; align-items: center; justify-content: center; }

  /* Section headings */
  .section-title { position: absolute; left: 0; width: 1200px; text-align: center; font-family: "Quicksand", sans-serif; font-weight: 700; font-size: 29px; letter-spacing: 3px; }
  .section-sub { position: absolute; left: 0; width: 1200px; text-align: center; font-family: "Quicksand", sans-serif; font-size: 14px; letter-spacing: 1.2px; }

  /* Categories */
  .tile { position: absolute; width: 152px; height: 156px; background: var(--gold-light); text-align: center; }
  .tile.is-hover { background: var(--cream); border: 1.5px solid var(--gold-light); box-shadow: 0 2px 6px rgba(0,0,0,.06); }
  .tile svg { position: absolute; left: 44px; top: 32px; }
  .tile-name { position: absolute; left: 0; top: 94px; width: 100%; font-family: "Quicksand", sans-serif; font-weight: 500; font-size: 16px; letter-spacing: .8px; }
  .tile-count { position: absolute; left: 0; top: 117px; width: 100%; font-family: "Quicksand", sans-serif; font-size: 9.5px; color: #555; letter-spacing: .6px; }

  /* Members */
  .members { position: absolute; left: 0; top: 1203px; width: 1200px; height: 825px; background: linear-gradient(180deg, var(--dark-top), #6b6b6b 30%, var(--dark-bottom)); }
  .members .section-title, .members .section-sub { color: var(--white); }
  .card { position: absolute; left: 156px; width: 531px; height: 94px; background: var(--gold); }
  .card-badge { position: absolute; left: 20px; top: 19px; width: 56px; height: 56px; border-radius: 50%; border: 2px solid var(--white); }
  .card-name { position: absolute; left: 126px; top: 24px; font-family: "Quicksand", sans-serif; font-weight: 600; font-size: 16px; letter-spacing: 1px; color: var(--white); }
  .card-meta { position: absolute; top: 55px; font-size: 9.5px; color: var(--white); display: flex; align-items: center; gap: 7px; font-family: "Quicksand", sans-serif; }
  .card-btn { position: absolute; left: 384px; top: 31px; width: 125px; height: 38px; border: 1.5px solid var(--ink); font-size: 8px; letter-spacing: .8px; display: flex; align-items: center; justify-content: center; color: var(--ink); }
  .map { position: absolute; left: 763px; top: 188px; width: 280px; height: 430px; background: linear-gradient(160deg, #eef0ec, #dfe6de 50%, #e9e6dc); }
  .all-btn { position: absolute; left: 484px; top: 705px; width: 232px; height: 37px; border: 1.5px solid #cfcfcf; color: var(--white); font-size: 8.5px; letter-spacing: .8px; display: flex; align-items: center; justify-content: center; }

  /* Footer */
  .footer { position: absolute; left: 0; top: 2028px; width: 1200px; height: 273px; background: var(--gold); color: var(--white); font-family: "Quicksand", sans-serif; }
  .footer-badge { position: absolute; left: 257px; top: 77px; width: 60px; height: 60px; border-radius: 50%; border: 2px solid var(--white); }
  .footer-head { position: absolute; top: 80px; font-weight: 700; font-size: 11px; letter-spacing: .4px; }
  .footer-text { position: absolute; left: 360px; top: 106px; width: 185px; font-size: 9px; line-height: 16px; }
  .footer-link { position: absolute; font-size: 9px; }
  .footer-about { left: 360px; top: 158px; text-decoration: underline; font-size: 9.5px; }
  .copyright { position: absolute; left: 0; top: 242px; width: 1200px; text-align: center; font-size: 7px; font-weight: 600; }
</style>
</head>
<body>

<header class="topbar">
  <div class="brand"><span class="brand-dot"></span><span class="brand-name">Wir bauen Brücken</span></div>
  <span class="nav-link is-active" style="left:287px">HOME</span>
  <span class="nav-link" style="left:362px">SUCHEN</span>
  <span class="nav-link" style="left:450px">ÜBER UNS</span>
  <span class="nav-link" style="left:544px">MITGLIEDSCHAFT</span>
  <span class="nav-link" style="left:675px">KONTAKT</span>
  <span class="social" style="left:823px"></span>
  <span class="social" style="left:842px"></span>
  <svg class="abs" style="left:860px;top:23px" width="14" height="14" viewBox="0 0 14 14"><circle cx="7" cy="4" r="3.3" fill="#fff"/><path d="M1 14c0-4 3-6 6-6s6 2 6 6z" fill="#fff"/></svg>
  <span class="nav-cta">MITGLIED WERDEN</span>
</header>

<section class="hero">
  <svg class="abs" style="left:640px;top:0" width="560" height="490" viewBox="0 0 560 490">
    <path d="M200 0 C70 90 0 220 60 490 L95 490 C30 260 80 110 230 0 Z" fill="var(--gold)"/>
    <path d="M230 0 C100 100 40 260 90 490 L106 490 C60 270 110 110 250 0 Z" fill="var(--gold-pale)"/>
    <path d="M250 0 L560 0 L560 490 L106 490 C60 270 110 110 250 0 Z" fill="#5a4a3a" role="img" aria-label="Foto: lächelnder Unternehmer mit Espressotasse in einem Café"/>
  </svg>
  <svg class="abs" style="left:746px;top:0" width="454" height="490" role="img" aria-label="Foto: lächelnder Unternehmer mit Espressotasse in einem Café">
    <defs><linearGradient id="photoTone" x1="0" y1="0" x2="1" y2="1"><stop offset="0" stop-color="#6b5a48"/><stop offset=".5" stop-color="#3f3a3c"/><stop offset="1" stop-color="#2c2a2c"/></linearGradient></defs>
    <path d="M144 0 L454 0 L454 490 L0 490 C-46 270 4 110 144 0 Z" fill="url(#photoTone)"/>
  </svg>
  <h1 class="hero-title">WIR BAUEN <span class="accent">BRÜCKEN</span></h1>
  <p class="hero-sub">Das Branchenverzeichnis der Selbstverantwortlichen</p>
  <p class="hero-text">Lorem ipsum dolor sit amet, consectetur adipisicing elit, sed do eiusmod tempor incididunt ut labore et dolore magna aliqua. Duis aute irure dolor in reprehenderit in voluptate velit esse cillum dolore eu fugiat nulla pariatur. Ut enim ad minim veniam, quis nostrud exercitation ullamco laboris nisi ut aliquip ex ea commodo!</p>
  <span class="btn btn-gold">UNTERNEHMER SUCHEN</span>
  <span class="btn btn-outline">MITGLIED WERDEN</span>
</section>

<form class="search">
  <label class="field" style="left:38px">Unternehmen, Name
    <svg width="17" height="16" viewBox="0 0 17 16"><path d="M8.5 1 L16 8 H14 V15 H10 V10 H7 V15 H3 V8 H1 Z" fill="var(--gold)"/></svg></label>
  <label class="field" style="left:257px">Stadt, PLZ oder Land
    <svg width="17" height="17" viewBox="0 0 17 17"><circle cx="8.5" cy="8.5" r="6" fill="none" stroke="var(--gold)" stroke-width="1.6"/><circle cx="8.5" cy="8.5" r="3" fill="var(--gold)"/><path d="M8.5 0v3M8.5 14v3M0 8.5h3M14 8.5h3" stroke="var(--gold)" stroke-width="1.4"/></svg></label>
  <label class="field" style="left:476px">Branche
    <svg width="14" height="14" viewBox="0 0 14 14"><path d="M2 5 L7 10 L12 5" fill="none" stroke="var(--gold)" stroke-width="1.8"/></svg></label>
  <span class="search-btn">SUCHEN</span>
</form>

<h2 class="section-title" style="top:664px">WIR ZEIGEN <span class="accent">BRANCHEN</span></h2>
<p class="section-sub" style="top:705px">Top 10 der gesuchten Unternehmenszweige.</p>

<svg width="0" height="0" style="position:absolute">
  <symbol id="people" viewBox="0 0 64 42"><circle cx="20" cy="9" r="8"/><circle cx="44" cy="9" r="7"/><path d="M0 42c0-11 8-18 20-18s20 7 20 18z"/><path d="M34 42c0-8 -2-13-5-16 4-2 9-3 14-3 12 0 21 6 21 19z"/></symbol>
</svg>

<div class="tile" style="left:163px;top:771px"><svg width="64" height="42" fill="#fff"><use href="#people"/></svg><div class="tile-name">Coaching</div><div class="tile-count">(23 Unternehmen)</div></div>
<div class="tile is-hover" style="left:347px;top:771px"><svg width="64" height="42" fill="var(--gold)"><use href="#people"/></svg><div class="tile-name">Consulting</div><div class="tile-count">(14 Unternehmen)</div></div>
<div class="tile" style="left:530px;top:771px"><svg width="64" height="42" fill="#fff"><use href="#people"/></svg><div class="tile-name">IT &amp; Marketing</div><div class="tile-count">(23 Unternehmen)</div></div>
<div class="tile" style="left:714px;top:771px"><svg width="64" height="42" fill="#fff"><use href="#people"/></svg><div class="tile-name">Logistik</div><div class="tile-count">(23 Unternehmen)</div></div>
<div class="tile" style="left:897px;top:771px"><svg width="64" height="42" fill="#fff"><use href="#people"/></svg><div class="tile-name">Bildung</div><div class="tile-count">(23 Unternehmen)</div></div>

<div class="tile" style="left:163px;top:976px"><svg width="64" height="42" fill="#fff"><use href="#people"/></svg><div class="tile-name">Coaching</div><div class="tile-count">(23 Unternehmen)</div></div>
<div class="tile" style="left:347px;top:976px"><svg width="64" height="42" fill="#fff"><use href="#people"/></svg><div class="tile-name">Coaching</div><div class="tile-count">(23 Unternehmen)</div></div>
<div class="tile" style="left:530px;top:976px"><svg width="64" height="42" fill="#fff"><use href="#people"/></svg><div class="tile-name">IT &amp; Marketing</div><div class="tile-count">(23 Unternehmen)</div></div>
<div class="tile" style="left:714px;top:976px"><svg width="64" height="42" fill="#fff"><use href="#people"/></svg><div class="tile-name">Logistik</div><div class="tile-count">(23 Unternehmen)</div></div>
<div class="tile" style="left:897px;top:976px"><svg width="64" height="42" fill="#fff"><use href="#people"/></svg><div class="tile-name">Bildung</div><div class="tile-count">(23 Unternehmen)</div></div>

<svg width="0" height="0" style="position:absolute">
  <symbol id="cal" viewBox="0 0 11 11"><rect x=".8" y="1.8" width="9.4" height="8.4" fill="none" stroke="#fff" stroke-width="1.4"/><rect x=".8" y="1.8" width="9.4" height="2.4" fill="#fff"/><rect x="2.5" y="5.5" width="2.5" height="2.5" fill="#fff"/></symbol>
  <symbol id="pin" viewBox="0 0 10 13"><path d="M5 0C2.2 0 0 2.2 0 5c0 3.5 5 8 5 8s5-4.5 5-8c0-2.8-2.2-5-5-5z" fill="#fff"/><circle cx="5" cy="5" r="1.8" fill="var(--gold)"/></symbol>
</svg>

<section class="members">
  <h2 class="section-title" style="top:73px">WIR ZEIGEN <span class="accent">UNTERNEHMER</span></h2>
  <p class="section-sub" style="top:112px">Unsere neuen UnternehmerInnen. Mach mit.</p>

  <article class="card" style="top:188px"><span class="card-badge"></span><div class="card-name">Firmenname</div>
    <div class="card-meta" style="left:126px"><svg width="11" height="11"><use href="#cal"/></svg>Coaching</div>
    <div class="card-meta" style="left:224px"><svg width="10" height="13"><use href="#pin"/></svg>München</div>
    <span class="card-btn">DETAILS</span></article>
  <article class="card" style="top:301px"><span class="card-badge"></span><div class="card-name">Firmenname</div>
    <div class="card-meta" style="left:126px"><svg width="11" height="11"><use href="#cal"/></svg>Coaching</div>
    <div class="card-meta" style="left:224px"><svg width="10" height="13"><use href="#pin"/></svg>München</div>
    <span class="card-btn">DETAILS</span></article>
  <article class="card" style="top:413px"><span class="card-badge"></span><div class="card-name">Firmenname</div>
    <div class="card-meta" style="left:126px"><svg width="11" height="11"><use href="#cal"/></svg>Coaching</div>
    <div class="card-meta" style="left:224px"><svg width="10" height="13"><use href="#pin"/></svg>München</div>
    <span class="card-btn">DETAILS</span></article>
  <article class="card" style="top:526px"><span class="card-badge"></span><div class="card-name">Firmenname</div>
    <div class="card-meta" style="left:126px"><svg width="11" height="11"><use href="#cal"/></svg>Coaching</div>
    <div class="card-meta" style="left:224px"><svg width="10" height="13"><use href="#pin"/></svg>München</div>
    <span class="card-btn">DETAILS</span></article>

  <div class="map" role="img" aria-label="Karte mit den Standorten der Mitgliedsunternehmen"></div>

  <span class="all-btn">ALLE UNTERNEHMEN ANZEIGEN</span>
</section>

<footer class="footer">
  <span class="footer-badge"></span>
  <div class="footer-head" style="left:360px">Wir bauen Brücken</div>
  <p class="footer-text">Duis sed odio sit amet nibh vulputate cursus a sit amet mauris. Morbi accumsan ipsum velit. Nam nec tellus a</p>
  <span class="footer-link footer-about">Über uns</span>

  <div class="footer-head" style="left:648px">WEBSITE</div>
  <span class="footer-link" style="left:648px;top:106px">Wir bauen Brücken</span>
  <span class="footer-link" style="left:648px;top:131px">Unternehmen suchen</span>
  <span class="footer-link" style="left:648px;top:156px">Mitgliedschaft</span>
  <span class="footer-link" style="left:648px;top:181px">Kontakt</span>

  <div class="footer-head" style="left:839px">RECHTLICHES</div>
  <span class="footer-link" style="left:839px;top:106px">Impressum</span>
  <span class="footer-link" style="left:839px;top:131px">Datenschutz</span>
  <span class="footer-link" style="left:839px;top:156px">AGB</span>
  <span class="footer-link" style="left:839px;top:181px">Sicherheitsbestimmungen</span>

  <p class="copyright">© 2020 Wir bauen Brücken</p>
</footer>

</body>
</html>
```